Water Delivery Service Website

We are working with BrivoNeté. They are a water delivery company and in need of a new website design.
Some sites to use for inspiration:
https://www.corvindale.example/home
https://www.plumtidego.example/en/home3
https://www.zelkop.example
https://www.hestrova.example
Thank you for taking the time to consider designing a website for us. We are web developers based in Stockton, CA, USA. Most of our projects go through the same process. Understanding this process may help you win a project with us. We custom-code all of our websites in-house. We don’t have any requirements as to what tools you use for your design, but we prefer Figma files. For any design that we label as four-stars, we send it to the client for review. The client picks the final design they want us to use. Once we complete this process, we will continue to show additional clients all the four-star sites and purchase them later. Your designs will have multiple chances to sell. For better chances of success, we ask that you follow these guidelines.
IMAGES:
If you use any images or icons in the design, we ask that you have a link to the asset so we can purchase the image/icon. Most of the designs we submit do not have the customer’s images on them unless they have some great images. Be creative; show us the feeling you are trying to portray with your image choices. Use any royalty-free site you choose. We subscribe to Quenlix and mainly use their images, but we can purchase images outside of Quenlix.
PLEASE NOTE: we will not submit designs to clients with watermarks on the images.
FONTS:
We ask that you identify the fonts used in the design. This can be done in a message if you want. We typically use Google Fonts and Quenlix Fonts.
CONTENT:
We're always open to different content and ideas. We often submit designs with stock images so the client can see our vision. We typically take pictures after the website launch to use their images with our vision. Lorem Ipsum is fine for paragraphs, but we ask that you write the headers in correct English. We want to be able to show the vision and identify the sections of the website.
INSPIRATION:
We typically add a couple of links in the brief of websites we like to help you get started in your design.
REVISIONS:
We do not often ask for revisions of the designs unless we see something in the design that may not appeal to the client. If there are slight changes that we want to make, we do that in the development process.
FEEDBACK:
We rarely give feedback on designs during the design process. We are working on many website projects and do not have the time to provide feedback. We usually respond if your request is well thought out and asks specific questions, but a note asking “feedback, please” usually goes unanswered.

```html
<!DOCTYPE html>
<html lang="en">
<head>
<meta charset="utf-8">
<title>BrivoNeté – Water Delivery</title>
<link rel="stylesheet" href="https://fonts.googleapis.com/css2?family=Ubuntu:wght@400;500;700&family=Poppins:wght@400;500;600&family=Tinos:wght@700&display=swap">
<style>
  :root{
    --navy:#1e2568;
    --navy-deep:#1b2160;
    --sky:#29abe2;
    --sky-light:#e3f3fa;
    --ink:#141414;
    --grey-bg:#f4f4f4;
    --white:#ffffff;
    --muted:#9a9a9a;
    --star:#f5b400;
    --heading:'Ubuntu', sans-serif;
    --body:'Poppins', sans-serif;
  }
  *{margin:0;padding:0;box-sizing:border-box}
  html,body{width:1200px;height:4202px;overflow:hidden}
  body{position:relative;font-family:var(--body);color:var(--ink);background:var(--white)}
  .abs{position:absolute}

  /* Header */
  .site-header{left:0;top:0;width:1200px;height:117px;background:var(--navy)}
  .brand{display:flex;align-items:center;gap:10px;color:var(--white)}
  .brand-dot{width:26px;height:26px;border-radius:50%;background:var(--white)}
  .brand-name{font-family:var(--heading);font-weight:400;font-size:36px;line-height:1}
  .brand-tag{font-family:var(--heading);font-size:13px;letter-spacing:3px;color:var(--white);margin-left:36px;margin-top:-2px}
  .main-nav a{position:absolute;top:48px;color:var(--white);font-size:14px;text-decoration:none;white-space:nowrap}
  .main-nav a.active::after{content:"";position:absolute;left:0;right:0;bottom:-9px;height:2px;background:var(--white)}

  /* Hero */
  .hero{left:0;top:117px;width:1200px;height:547px;background:linear-gradient(110deg,#dff1f8 0%,#eef8fc 45%,#f4fbfe 100%)}
  .hero-photo{left:685px;top:117px;width:515px;height:547px;background:radial-gradient(ellipse at 55% 55%,#7fc8e6 0%,#bfe3f2 35%,rgba(230,246,252,0) 70%)}
  .hero-title{left:98px;top:232px;font-family:var(--heading);font-size:80px;line-height:80px}
  .hero-title .light{color:var(--sky);font-weight:400;display:block}
  .hero-title .strong{color:var(--ink);font-weight:700;display:block}
  .hero-text{left:108px;top:412px;width:560px;font-size:12px;line-height:21px;color:var(--ink)}
  .btn{display:inline-flex;align-items:center;justify-content:center;border-radius:40px;color:var(--white);text-decoration:none;font-family:var(--body)}
  .btn-hero{left:95px;top:471px;width:152px;height:54px;background:var(--navy);font-size:16px}

  /* Section titles */
  .section-title{width:1200px;left:0;text-align:center;font-family:var(--heading);font-weight:400;font-size:42px;color:var(--navy)}
  .rule{height:3px;background:var(--sky)}

  /* Why choose */
  .feature{width:260px;text-align:center}
  .feature-icon{width:140px;height:140px;border-radius:50%;background:var(--sky);margin:0 auto;display:flex;align-items:center;justify-content:center}
  .feature-label{margin-top:30px;font-family:var(--heading);font-size:21px;color:var(--ink)}

  /* Grey band */
  .grey-band{left:0;top:1161px;width:1200px;height:1370px;background:var(--grey-bg)}
  .about-title{left:130px;top:1300px;font-family:var(--heading);font-size:44px;color:var(--navy);font-weight:400}
  .about-text{left:130px;top:1388px;width:508px;font-size:13.5px;line-height:23.5px;text-align:justify;color:#333}
  .btn-small{background:var(--sky);font-size:13px}
  .photo-ring{border:2px solid var(--navy);border-radius:50%;display:flex;align-items:center;justify-content:center;background:var(--white)}
  .photo-ring .photo{border-radius:50%}

  /* Products */
  .product-card{width:313px;height:476px;background:var(--white);box-shadow:0 2px 10px rgba(0,0,0,.12);text-align:center}
  .product-photo{margin:15px 12px 0;height:281px;border-radius:6px}
  .product-name{margin-top:32px;font-size:16px;color:var(--navy)}
  .product-price{margin-top:6px;font-family:'Tinos',serif;font-weight:700;font-size:19px;color:var(--ink)}
  .stars{color:var(--star);font-size:15px;letter-spacing:1px;margin-top:2px}
  .btn-product{margin-top:10px;width:126px;height:34px;background:var(--sky);font-size:14px}
  .dots{left:570px;top:2439px;display:flex;gap:4px}
  .dots span{width:12px;height:12px;border-radius:50%;background:#8c93b8}
  .dots span.on{background:var(--navy)}

  /* Testimonials */
  .quote-mark{left:0;width:1200px;top:2740px;text-align:center;font-family:Georgia,serif;font-weight:700;font-size:220px;line-height:220px;color:var(--navy)}
  .quote-text{left:260px;top:2882px;width:680px;text-align:center;font-size:15.5px;line-height:25px;color:#222}
  .quote-name{left:0;width:1200px;top:2984px;text-align:center;font-weight:600;font-size:16px;color:var(--ink)}
  .quote-stars{left:0;width:1200px;top:3010px;text-align:center;color:var(--star);font-size:24px;letter-spacing:2px}
  .arrow{width:36px;height:36px;border-radius:4px;display:flex;align-items:center;justify-content:center}

  /* Contact */
  .contact-title{left:96px;top:3232px;font-family:var(--heading);font-size:44px;font-weight:400;color:var(--navy)}
  .contact-intro{left:101px;top:3344px;font-size:14px;color:#333}
  .field{height:47px;background:var(--white);box-shadow:0 1px 6px rgba(0,0,0,.12);font-size:13px;color:#b5b5b5;padding:16px 10px}
  .btn-send{left:88px;top:3609px;width:112px;height:37px;background:var(--sky);font-size:16px}

  /* Footer */
  .site-footer{left:0;top:3748px;width:1200px;height:454px;background:var(--navy)}
  .footer-heading{font-size:20px;color:var(--white);font-weight:400}
  .footer-links li{list-style:none;position:relative;padding-left:30px;color:var(--white);font-size:14px;height:32.5px}
  .footer-links li::before{content:"";position:absolute;left:0;top:7px;width:7px;height:7px;border-radius:50%;background:var(--white)}
  .contact-row{display:flex;gap:14px;color:var(--white);font-size:14px;line-height:24px}
  .contact-icon{width:36px;height:36px;border-radius:50%;background:var(--white);flex:none;display:flex;align-items:center;justify-content:center}
  .social{display:flex;gap:12px}
  .social span{width:37px;height:37px;border-radius:50%;background:var(--white)}
  .footer-rule{left:73px;top:4126px;width:1063px;height:1px;background:rgba(255,255,255,.35)}
  .footer-small{top:4150px;color:var(--white);font-size:13.5px}
</style>
</head>
<body>

<!-- Header -->
<header class="site-header abs">
  <div class="abs" style="left:72px;top:34px">
    <div class="brand"><span class="brand-dot"></span><span class="brand-name">BrivoNeté</span></div>
    <div class="brand-tag">water delivery</div>
  </div>
  <nav class="main-nav">
    <a class="active" href="#" style="left:369px">Home</a>
    <a href="#" style="left:442px">Who we are</a>
    <a href="#" style="left:561px">Hesychasm</a>
    <a href="#" style="left:682px">Courses</a>
    <a href="#" style="left:778px">Coffee</a>
    <a href="#" style="left:850px">Shop</a>
    <a href="#" style="left:922px">Contact Us</a>
  </nav>
  <svg class="abs" style="left:1076px;top:47px" width="22" height="22" viewBox="0 0 22 22" fill="none" stroke="#fff" stroke-width="2"><circle cx="9" cy="9" r="7"/><path d="M14 14l6 6"/></svg>
  <svg class="abs" style="left:1112px;top:45px" width="20" height="24" viewBox="0 0 20 24" fill="none" stroke="#fff" stroke-width="2"><rect x="2" y="7" width="16" height="15" rx="1"/><path d="M6 9V5a4 4 0 0 1 8 0v4"/></svg>
</header>

<!-- Hero -->
<section class="hero abs"></section>
<div class="hero-photo abs" role="img" aria-label="Plastic water bottle with a splash of water around it"></div>
<h1 class="hero-title abs"><span class="light">Pure &amp; Healty</span><span class="strong">Drinking Water</span></h1>
<p class="hero-text abs">Lorem ipsum dolor sit amet, consectetur adipiscing elit, sed do eiusmod tempor incididunt ut labore et dolore magna aliqua. Quis ipsum suspendisse ultrices gravida. Risus commodo viverra</p>
<a class="btn btn-hero abs" href="#">Shop Now</a>

<!-- Why choose us -->
<h2 class="section-title abs" style="top:752px">Why Choose Us</h2>
<div class="rule abs" style="left:550px;top:819px;width:100px"></div>

<div class="feature abs" style="left:82px;top:869px">
  <div class="feature-icon">
    <svg width="140" height="140" viewBox="0 0 140 140" fill="none" stroke="#fff" stroke-width="2.5"><circle cx="70" cy="70" r="56" stroke-dasharray="2 5"/><path d="M72 40c10 14 18 24 18 34a18 18 0 0 1-36 0c0-10 8-20 18-34z"/></svg>
  </div>
  <div class="feature-label">Maxium Purity</div>
</div>
<div class="feature abs" style="left:340px;top:869px">
  <div class="feature-icon">
    <svg width="140" height="140" viewBox="0 0 140 140" fill="none" stroke="#fff" stroke-width="2.5"><circle cx="70" cy="70" r="56" stroke-dasharray="2 5"/><path d="M44 62h52M50 62l8 22h24l8-22"/><path d="M70 38c6 8 9 12 9 16a9 9 0 0 1-18 0c0-4 3-8 9-16z"/></svg>
  </div>
  <div class="feature-label">5 Steps Filtration</div>
</div>
<div class="feature abs" style="left:597px;top:869px">
  <div class="feature-icon">
    <svg width="140" height="140" viewBox="0 0 140 140" fill="none" stroke="#fff" stroke-width="2.5"><circle cx="70" cy="70" r="56" stroke-dasharray="2 5"/><path d="M63 46h14M65 46v16l-12 22h34L75 62V46"/></svg>
  </div>
  <div class="feature-label">Cholorine Free</div>
</div>
<div class="feature abs" style="left:855px;top:869px">
  <div class="feature-icon">
    <svg width="140" height="140" viewBox="0 0 140 140" fill="none" stroke="#fff" stroke-width="2.5"><circle cx="70" cy="70" r="56" stroke-dasharray="2 5"/><circle cx="70" cy="62" r="18"/><path d="M62 62l6 6 11-12M60 78l-6 18 10-4 6 8 2-20M80 78l6 18-10-4-6 8"/></svg>
  </div>
  <div class="feature-label">Quality Certified</div>
</div>

<!-- About -->
<section class="grey-band abs"></section>
<h2 class="about-title abs">About Us</h2>
<div class="rule abs" style="left:130px;top:1360px;width:108px"></div>
<p class="about-text abs">Sed ut perspiciatis unde omnis iste natus error sit voluptatem accusantium doloremque laudantium, totam rem aperiam, eaque ipsa quae ab illo inventore veritatis et quasi architecto beatae vitae dicta sunt explicabo. Nemo enim ipsam voluptatem quia voluptas sit aspernatur aut odit aut fugit, sed quia consequuntur magni dolores eos qui ratione voluptatem sequi nesciunt.</p>
<a class="btn btn-small abs" href="#" style="left:132px;top:1551px;width:106px;height:30px">Read More</a>
<div class="photo-ring abs" style="left:699px;top:1246px;width:402px;height:402px">
  <div class="photo" role="img" aria-label="Glass water bottle standing on a wet dark surface" style="width:388px;height:388px;background:radial-gradient(circle at 50% 40%,#3e6a8a 0%,#1b3550 55%,#0c1a2a 100%)"></div>
</div>

<!-- Products -->
<h2 class="section-title abs" style="top:1795px">Our Products</h2>
<div class="rule abs" style="left:550px;top:1854px;width:103px"></div>

<div class="product-card abs" style="left:91px;top:1915px">
  <div class="product-photo" role="img" aria-label="Water bottle against a blue sky and sea" style="background:linear-gradient(180deg,#6fb6e6 0%,#a4d3ef 55%,#2f6e7a 80%,#1aa2e0 100%)"></div>
  <div class="product-name">Product 1</div>
  <div class="product-price">$10.00</div>
  <div class="stars">★★★★☆</div>
  <a class="btn btn-product" href="#">Shop Now</a>
</div>
<div class="product-card abs" style="left:446px;top:1915px">
  <div class="product-photo" role="img" aria-label="Clear water bottle on a white background" style="background:linear-gradient(180deg,#f4f5f7 0%,#e6e8eb 75%,#d9dcdf 100%)"></div>
  <div class="product-name">Product 2</div>
  <div class="product-price">$10.00</div>
  <div class="stars">★★★★☆</div>
  <a class="btn btn-product" href="#">Shop Now</a>
</div>
<div class="product-card abs" style="left:801px;top:1915px">
  <div class="product-photo" role="img" aria-label="Large blue water cooler jug" style="background:radial-gradient(ellipse at 50% 50%,#5fb4ec 0%,#a7d6f5 40%,#ffffff 72%);box-shadow:inset 0 0 0 1px #eee"></div>
  <div class="product-name">Product 3</div>
  <div class="product-price">$10.00</div>
  <div class="stars">★★★★☆</div>
  <a class="btn btn-product" href="#">Shop Now</a>
</div>
<div class="dots abs"><span></span><span></span><span class="on"></span><span></span></div>

<!-- Testimonials -->
<h2 class="section-title abs" style="top:2634px">Our Testimonials</h2>
<div class="rule abs" style="left:547px;top:2699px;width:105px"></div>
<div class="quote-mark abs">&#8220;</div>
<p class="quote-text abs">Lorem ipsum dolor sit amet, consectetur adipiscing elit, sed do eiusmod tempor incididunt ut labore et dolore magna aliqua. Quis ipsum suspendisse ultrices gravida. Risus commodo viverra maecenas accumsan lacus vel facilisis.</p>
<div class="quote-name abs">MARLO VENKERT</div>
<div class="quote-stars abs">★★★★★</div>
<div class="arrow abs" style="left:173px;top:2890px;background:#bfe2f3">
  <svg width="14" height="14" viewBox="0 0 14 14" fill="none" stroke="#fff" stroke-width="2"><path d="M9 2L4 7l5 5"/></svg>
</div>
<div class="arrow abs" style="left:990px;top:2890px;background:var(--sky)">
  <svg width="14" height="14" viewBox="0 0 14 14" fill="none" stroke="#fff" stroke-width="2"><path d="M5 2l5 5-5 5"/></svg>
</div>

<!-- Contact -->
<h2 class="contact-title abs">Contact Us</h2>
<div class="rule abs" style="left:101px;top:3293px;width:106px"></div>
<p class="contact-intro abs">For more information Please fill out the following and we will be in touch shortly</p>
<div class="field abs" style="left:96px;top:3396px;width:266px">First Name</div>
<div class="field abs" style="left:390px;top:3396px;width:267px">Last Name</div>
<div class="field abs" style="left:96px;top:3469px;width:266px">Phone</div>
<div class="field abs" style="left:390px;top:3469px;width:267px">Company Name</div>
<div class="field abs" style="left:96px;top:3538px;width:561px">Email</div>
<a class="btn btn-send abs" href="#">Send</a>
<div class="photo-ring abs" style="left:707px;top:3256px;width:416px;height:416px">
  <div class="photo" role="img" aria-label="Glass of water with splashing water and bubbles" style="width:390px;height:390px;background:radial-gradient(circle at 50% 55%,#eaf6fb 0%,#9ccfe4 45%,#5fb2d4 100%)"></div>
</div>

<!-- Footer -->
<footer class="site-footer abs">
  <div class="abs" style="left:139px;top:170px">
    <div class="brand"><span class="brand-dot" style="width:30px;height:30px"></span><span class="brand-name" style="font-size:44px">BrivoNeté</span></div>
    <div class="brand-tag" style="font-size:15px;margin-left:40px">water delivery</div>
  </div>
  <div class="social abs" style="left:196px;top:258px" aria-label="Social media links">
    <span></span><span></span><span></span>
  </div>

  <h3 class="footer-heading abs" style="left:543px;top:104px">LINKS</h3>
  <div class="rule abs" style="left:543px;top:138px;width:63px;height:1px;background:#fff"></div>
  <ul class="footer-links abs" style="left:543px;top:178px">
    <li>About Us</li><li>Our Services</li><li>Our Products</li><li>Testimonials</li><li>Contact Us.</li>
  </ul>

  <h3 class="footer-heading abs" style="left:799px;top:104px">CONTACT US</h3>
  <div class="rule abs" style="left:799px;top:138px;width:100px;height:1px;background:#fff"></div>
  <div class="contact-row abs" style="left:796px;top:172px">
    <span class="contact-icon"><svg width="16" height="18" viewBox="0 0 16 18"><path d="M8 1a6 6 0 0 0-6 6c0 5 6 10 6 10s6-5 6-10a6 6 0 0 0-6-6z" fill="#1e2568"/><circle cx="8" cy="7" r="2.2" fill="#fff"/></svg></span>
    <span>465, Lorem Ipsum<br>Lorem Ipsum , Lorem Ipsum</span>
  </div>
  <div class="contact-row abs" style="left:796px;top:236px;align-items:center">
    <span class="contact-icon"><svg width="16" height="16" viewBox="0 0 16 16"><path d="M3 1l3 3-2 2c1 2 3 4 5 5l2-2 3 3-2 3C6 14 2 10 1 3z" fill="#1e2568"/></svg></span>
    <span>+1 888 888 8888</span>
  </div>
  <div class="contact-row abs" style="left:796px;top:288px;align-items:center">
    <span class="contact-icon"><svg width="18" height="14" viewBox="0 0 18 14" fill="none" stroke="#1e2568" stroke-width="1.8"><rect x="1" y="1" width="16" height="12" rx="1"/><path d="M1 2l8 6 8-6"/></svg></span>
    <span>info@companyname.com</span>
  </div>
</footer>
<div class="footer-rule abs"></div>
<div class="footer-small abs" style="left:73px">Copyright © 2025 All Rights Reserved By Company Name</div>
<div class="footer-small abs" style="left:905px">Privacy policy Terms &amp; conditions</div>

</body>
</html>
```